torvik buying grid and torvik website header | ||
torvik boxes madein AI AND PHOTOSHOP BUYING TABLE OR HEADER | ||
TORVIK, Harder is Better | ||
Let her rideyour Torvik tonight | ||
Health | ||
www.torvikvit.com | ||
YES | ||
Torvik is a High Quality mens sexua lhealth supplement,that need high quality graffics and marketing material and high-end science and proffesional credible look | ||
We need a great header built for many types of websites but with an overall branding look and feel,buta header done in both AI and PHOTOSHOP and Readable by Plimbo spider. WE alsoneed our torvik box design done in a 3-D photoshop and AI high resolution image and also make a buying grid table to have many special buying promotional options specials all in one table area,that will be in HTML and have Buy Buttons live and attached to shopping cart |
Cutting-Edge Unique/Creative Flashy Professional Futuristic Trendy Content Driven Exciting Corporate Modern Colorful High Tech Masculine |
blues,light and dark, light purplesfusia or plum | ||
silver,metalic,brushed stainless steal,charcoal | ||
reds oranges, yellows | ||

```html
<!DOCTYPE html>
<html lang="en">
<head>
<meta charset="utf-8">
<title>Torvik — Web Banner Set</title>
<link rel="stylesheet" href="https://fonts.googleapis.com/css2?family=Russo+One&family=Roboto:wght@700;900&display=swap">
<style>
  :root {
    --steel-light: #e4e6e8;
    --steel-mid: #c9ccd0;
    --steel-dark: #a9adb2;
    --plum-light: #d46fd8;
    --plum: #a43bb4;
    --plum-deep: #6b1f86;
    --logo-purple: #6a2c91;
    --white: #ffffff;
    --cta-red: #e0201c;
    --cta-red-dark: #a50f0c;
    --seal-red: #d9261c;
    --seal-blue: #1d4fa3;
    --box-navy: #1b2350;
    --box-blue: #3a5fb0;
  }
  * { box-sizing: border-box; margin: 0; padding: 0; }
  html, body { width: 1200px; height: 840px; overflow: hidden; }
  body {
    position: relative;
    background: linear-gradient(100deg, var(--steel-dark) 0%, var(--steel-light) 35%, var(--steel-mid) 60%, var(--steel-light) 80%, var(--steel-dark) 100%);
    font-family: "Russo One", sans-serif;
  }
  .banner {
    position: absolute;
    overflow: hidden;
    background: linear-gradient(165deg, var(--plum-light) 0%, var(--plum) 50%, var(--plum-deep) 100%);
    box-shadow: 0 3px 8px rgba(0,0,0,.35);
    color: var(--white);
  }
  .banner .glow { position: absolute; inset: 0; width: 100%; height: 100%; }
  .brand {
    position: absolute;
    font-family: "Russo One", sans-serif;
    color: var(--logo-purple);
    line-height: 1;
    z-index: 2;
  }
  .headline {
    position: absolute;
    font-family: "Russo One", sans-serif;
    font-weight: 400;
    line-height: 1;
    white-space: nowrap;
    text-shadow: 0 2px 3px rgba(60,0,80,.55);
    z-index: 2;
  }
  .headline .small { font-size: .7em; }
  .seal {
    position: absolute;
    border-radius: 50%;
    background: radial-gradient(circle, var(--seal-red) 0 55%, var(--white) 56% 64%, var(--seal-blue) 65%);
    box-shadow: 0 2px 4px rgba(0,0,0,.35);
    z-index: 1;
  }
  .product-shot {
    position: absolute;
    border-radius: 3px;
    background: linear-gradient(150deg, var(--box-blue) 0%, var(--box-navy) 55%, #0c1030 100%);
    box-shadow: 0 3px 6px rgba(0,0,0,.45);
  }
  .buy-button {
    position: absolute;
    display: flex; align-items: center; justify-content: center;
    border-radius: 14px;
    background: linear-gradient(180deg, #ff5a4e 0%, var(--cta-red) 50%, var(--cta-red-dark) 100%);
    border: 2px solid var(--white);
    font-family: "Roboto", sans-serif; font-weight: 900;
    font-size: 12px; color: var(--white); letter-spacing: .5px;
    box-shadow: 0 2px 3px rgba(0,0,0,.4);
    z-index: 2;
  }
  .site-url {
    position: absolute;
    font-family: "Roboto", sans-serif; font-weight: 700;
    font-size: 10px; color: var(--white); letter-spacing: .3px;
    z-index: 2;
  }

  /* Skyscrapers */
  .skyscraper { top: 149px; width: 144px; height: 571px; }
  .skyscraper--harder { left: 127px; }
  .skyscraper--ride { left: 283px; width: 149px; }
  .skyscraper .brand { top: 22px; left: 12px; font-size: 30px; }
  .skyscraper--harder .headline { top: 150px; left: 0; width: 100%; text-align: center; font-size: 29px; }
  .skyscraper--ride .headline { top: 112px; left: 0; width: 100%; text-align: center; font-size: 23px; line-height: 1.15; }
  .skyscraper .product-shot { left: 14px; top: 345px; width: 118px; height: 140px; }
  .skyscraper .site-url { bottom: 14px; left: 0; width: 100%; text-align: center; }
  .skyscraper--harder .seal { left: 36px; top: 272px; width: 70px; height: 70px; }
  .skyscraper--ride .buy-button { left: 38px; top: 282px; width: 74px; height: 26px; }

  /* Leaderboards */
  .leaderboard { left: 451px; width: 622px; }
  .leaderboard--harder { top: 149px; height: 79px; }
  .leaderboard--ride { top: 240px; height: 74px; }
  .leaderboard .brand { top: 20px; left: 14px; font-size: 32px; }
  .leaderboard--harder .headline { top: 24px; left: 168px; font-size: 21px; }
  .leaderboard--ride .headline { top: 12px; left: 168px; font-size: 20px; line-height: 1.1; }
  .leaderboard--harder .product-shot { left: 398px; top: 10px; width: 122px; height: 56px; }
  .leaderboard--harder .seal { left: 534px; top: 8px; width: 40px; height: 40px; }
  .leaderboard--ride .product-shot { left: 392px; top: 10px; width: 130px; height: 56px; }
  .leaderboard .site-url { right: 16px; bottom: 8px; }
  .leaderboard--ride .buy-button { left: 532px; top: 12px; width: 78px; height: 26px; }

  /* Medium rectangles */
  .rectangle { top: 461px; width: 269px; height: 259px; }
  .rectangle--harder { left: 451px; }
  .rectangle--ride { left: 737px; width: 271px; }
  .rectangle .brand { top: 16px; right: 12px; font-size: 28px; }
  .rectangle--harder .headline { top: 22px; left: 14px; font-size: 26px; line-height: 1.1; }
  .rectangle--ride .headline { top: 20px; left: 14px; font-size: 22px; line-height: 1.15; }
  .rectangle--harder .seal { left: 28px; top: 150px; width: 62px; height: 62px; }
  .rectangle .product-shot { right: 14px; top: 92px; width: 140px; height: 118px; }
  .rectangle--ride .product-shot { top: 100px; width: 134px; height: 112px; }
  .rectangle--ride .buy-button { left: 16px; top: 176px; width: 80px; height: 26px; }
  .rectangle .site-url { right: 14px; bottom: 12px; }
</style>
</head>
<body>

  <section class="banner skyscraper skyscraper--harder">
    <svg class="glow" viewBox="0 0 144 571" preserveAspectRatio="none" aria-hidden="true">
      <polygon points="0,0 144,0 144,62 0,80" fill="#fff"/>
      <polygon points="0,120 144,60 144,130 0,200" fill="#fff" opacity=".12"/>
    </svg>
    <div class="brand">Torvik</div>
    <h2 class="headline">HARDER<br><span class="small">is</span><br>Better</h2>
    <div class="seal" role="img" aria-label="Satisfaction seal"></div>
    <div class="product-shot" role="img" aria-label="Torvik supplement boxes"></div>
    <div class="site-url">WWW.TORVIKVIT.COM</div>
  </section>

  <section class="banner skyscraper skyscraper--ride">
    <svg class="glow" viewBox="0 0 149 571" preserveAspectRatio="none" aria-hidden="true">
      <polygon points="0,0 149,0 149,62 0,80" fill="#fff"/>
      <polygon points="0,120 149,60 149,130 0,200" fill="#fff" opacity=".12"/>
    </svg>
    <div class="brand">Torvik</div>
    <h2 class="headline">Let her<br>ride your<br>Torvik<br>tonight</h2>
    <div class="buy-button">BUY NOW</div>
    <div class="product-shot" role="img" aria-label="Torvik supplement boxes"></div>
    <div class="site-url">WWW.TORVIKVIT.COM</div>
  </section>

  <section class="banner leaderboard leaderboard--harder">
    <svg class="glow" viewBox="0 0 622 79" preserveAspectRatio="none" aria-hidden="true">
      <polygon points="0,0 158,0 140,79 0,79" fill="#fff"/>
      <polygon points="300,79 380,0 470,0 390,79" fill="#fff" opacity=".12"/>
    </svg>
    <div class="brand">Torvik</div>
    <h2 class="headline">HARDER <span class="small">is</span> Better</h2>
    <div class="product-shot" role="img" aria-label="Torvik supplement boxes"></div>
    <div class="seal" role="img" aria-label="Satisfaction seal"></div>
    <div class="site-url">WWW.TORVIKVIT.COM</div>
  </section>

  <section class="banner leaderboard leaderboard--ride">
    <svg class="glow" viewBox="0 0 622 74" preserveAspectRatio="none" aria-hidden="true">
      <polygon points="0,0 158,0 140,74 0,74" fill="#fff"/>
      <polygon points="300,74 380,0 470,0 390,74" fill="#fff" opacity=".12"/>
    </svg>
    <div class="brand">Torvik</div>
    <h2 class="headline">Let her ride your<br>Torvik tonight</h2>
    <div class="product-shot" role="img" aria-label="Torvik supplement boxes"></div>
    <div class="buy-button">BUY NOW</div>
    <div class="site-url">WWW.TORVIKVIT.COM</div>
  </section>

  <section class="banner rectangle rectangle--harder">
    <svg class="glow" viewBox="0 0 269 259" preserveAspectRatio="none" aria-hidden="true">
      <polygon points="160,0 269,0 269,58 150,66" fill="#fff"/>
      <polygon points="0,200 269,90 269,150 0,260" fill="#fff" opacity=".1"/>
    </svg>
    <div class="brand">Torvik</div>
    <h2 class="headline">HARDER<br><span class="small">is</span><br>Better</h2>
    <div class="seal" role="img" aria-label="Satisfaction seal"></div>
    <div class="product-shot" role="img" aria-label="Torvik supplement boxes"></div>
    <div class="site-url">WWW.TORVIKVIT.COM</div>
  </section>

  <section class="banner rectangle rectangle--ride">
    <svg class="glow" viewBox="0 0 271 259" preserveAspectRatio="none" aria-hidden="true">
      <polygon points="160,0 271,0 271,58 150,66" fill="#fff"/>
      <polygon points="0,200 271,90 271,150 0,260" fill="#fff" opacity=".1"/>
    </svg>
    <div class="brand">Torvik</div>
    <h2 class="headline">Let her<br>ride your<br>Torvik<br>tonight</h2>
    <div class="buy-button">BUY NOW</div>
    <div class="product-shot" role="img" aria-label="Torvik supplement boxes"></div>
    <div class="site-url">WWW.TORVIKVIT.COM</div>
  </section>

</body>
</html>
```